Touring Cabaret Seasons Needs a Poster Design

We need a poster design for upcoming Cabaret seasons in Melbourne and Adelaide (Australia) for a prestigious festival.

Show is titled "Here's a Small Thing I Dreamed Up Last Week..." and is a comedy parody of bad cabaret and deluded performers. We'd like the poster to reflect the comedy of the piece without being silly and inaccessable.

Artist has recently won awards for this show and these will need to be listed as a part of the design.

I have attached a couple of photographs that can be used - one is the artist with a blank book cover and these could be used to overlay text.

Would like it to not look too wordy, however I realise we've asked for a lot of text to be included.

Target Market(s)

Ages 20 - 40 cabaret or comedy fans.

Industry/Entity Type

Festival

Requirements
Must have
• TEXT:
The Velvet Parlour presents:
Here's a Small Thing I Dreamed Up Last Week...

TEXT:
WINNER of BEST CABARET, BEST WRITING and PEOPLE’S CHOICE awards at Quick + Tidy Revue 2011

TEXT:
The Lantern Room (Melbourne)
Feb 23rd to the 26th

Le Corbeau, REVedge(Adelaide)
March 3rd and 4th

QUOTES:
“...the funniest things in spandex. 4.5 stars” – The Courier Post on Rally! A revue about lawn bowls.

“a clever dissection of bad cabaret” – Owen Blackwood, The Courier Post on Quick + Tidy Revue
Nice to have
• TEXT:
The last time someone showed you a little something they were working on, did you lose an hour of your life you will never get back? Don’t worry – we’ve all been there.

TEXT:
Composer and co-writer of Rally! (A revue about lawn bowls) and WINNER of BEST CABARET, BEST WRITING and PEOPLE’S CHOICE awards at Quick + Tidy Revue 2011, presents her full show, with more original music and helpful anecdotes.

WEBSITE:
More info at www.mingleface.example/thevelvetparlour

```html
<!DOCTYPE html>
<html lang="en">
<head>
<meta charset="utf-8">
<title>Here's a Small Thing I Dreamed Up Last Week... — The Velvet Parlour</title>
<link rel="stylesheet" href="https://fonts.googleapis.com/css2?family=Crimson+Text:wght@400;600;700&family=Rye&display=swap">
<style>
  :root {
    --copper: #c48a45;
    --copper-dark: #a8702f;
    --rust: #b0562c;
    --ink: #050505;
    --paper: #ffffff;
    --gold-text: #d7a354;
  }
  * { margin: 0; padding: 0; box-sizing: border-box; }
  html, body { width: 848px; height: 1200px; overflow: hidden; background: var(--ink); }
  .poster {
    position: relative; width: 848px; height: 1200px; overflow: hidden;
    background: var(--ink);
    font-family: "Crimson Text", Georgia, serif; color: var(--paper);
  }
  .stage-photo {
    position: absolute; inset: 0;
    background:
      radial-gradient(ellipse 230px 330px at 360px 420px, #7a4f36 0%, #3a2418 45%, transparent 80%),
      radial-gradient(ellipse 160px 120px at 70px 640px, #8a6a2a 0%, transparent 75%),
      radial-gradient(ellipse 520px 700px at 380px 560px, #1c120c 0%, var(--ink) 70%);
  }
  .bands { position: absolute; inset: 0; }
  .award-banner {
    position: absolute; left: 50px; top: 36px;
    transform: rotate(-7deg); transform-origin: left top;
    line-height: 1;
  }
  .award-banner__winner { font-size: 44px; font-weight: 700; letter-spacing: 1px; }
  .award-banner__detail { font-size: 23px; line-height: 1.1; margin-top: 2px; }
  .reviews {
    position: absolute; right: 50px; top: 160px; width: 320px;
    text-align: right; transform: rotate(-7deg); transform-origin: right top;
  }
  .review { margin-bottom: 14px; }
  .review__quote { font-size: 26px; line-height: 1.05; }
  .review__source { font-size: 11px; margin-top: 6px; }
  .presenter {
    position: absolute; left: 390px; top: 575px;
    font-size: 25px; color: var(--gold-text);
    transform: rotate(-7deg); transform-origin: left top;
  }
  .show-title {
    position: absolute; left: 330px; top: 640px; width: 520px;
    font-family: "Rye", serif; font-weight: 400;
    font-size: 46px; line-height: 1.15; text-transform: uppercase;
    color: var(--paper);
    -webkit-text-stroke: 1.5px var(--ink);
    text-shadow: 3px 3px 0 var(--ink), 5px 5px 0 var(--paper), 6px 6px 0 var(--ink);
    transform: rotate(-7deg); transform-origin: left top;
  }
  .dates {
    position: absolute; right: 38px; top: 870px; width: 380px;
    text-align: right; transform: rotate(-7deg); transform-origin: right top;
  }
  .date-entry { margin-bottom: 12px; }
  .date-entry__venue { font-size: 22px; line-height: 1.1; }
  .date-entry__when { font-size: 29px; line-height: 1.1; }
  .blurb {
    position: absolute; left: 22px; top: 908px; width: 415px; height: 190px;
    background: var(--rust); padding: 14px 14px 14px 105px;
    transform: rotate(-7deg); transform-origin: left top;
    font-size: 13px; line-height: 1.22;
  }
  .blurb p + p { margin-top: 9px; }
  .blurb__photo {
    position: absolute; left: 10px; top: 40px; width: 84px; height: 124px;
    background: linear-gradient(160deg, #e8e4df, #b8b0a8);
  }
  .more-info {
    position: absolute; right: 40px; bottom: 56px;
    font-size: 15px; white-space: nowrap;
    transform: rotate(-6deg); transform-origin: right bottom;
  }
</style>
</head>
<body>
<main class="poster">
  <div class="stage-photo" role="img" aria-label="Stage photograph of a performer in a strapless black gown and gold glove singing at a microphone against a black backdrop"></div>

  <svg class="bands" width="848" height="1200" viewBox="0 0 848 1200" aria-hidden="true">
    <polygon points="0,0 848,0 848,66 0,170" fill="var(--copper)"/>
    <line x1="0" y1="174" x2="848" y2="70" stroke="var(--paper)" stroke-width="5"/>
    <polygon points="0,1200 848,1108 848,1200" fill="var(--copper-dark)"/>
    <line x1="0" y1="1198" x2="848" y2="1104" stroke="var(--paper)" stroke-width="5"/>
  </svg>

  <header class="award-banner">
    <div class="award-banner__winner">WINNER!</div>
    <div class="award-banner__detail">BEST CABARET, BEST WRITING and PEOPLE’S<br>CHOICE awards at Quick + Tidy Revue 2011</div>
  </header>

  <section class="reviews">
    <blockquote class="review">
      <p class="review__quote">“...the funniest things in<br>spandex. 4.5 stars”</p>
      <p class="review__source">– The Courier Post on Rally! A revue about lawn bowls.</p>
    </blockquote>
    <blockquote class="review">
      <p class="review__quote">“a clever dissection of<br>bad cabaret”</p>
      <p class="review__source">– Owen Blackwood, The Courier Post on Quick + Tidy Revue</p>
    </blockquote>
  </section>

  <p class="presenter">The Velvet Parlour presents:</p>
  <h1 class="show-title">Here's a small<br>thing I dreamed<br>up last week...</h1>

  <section class="dates">
    <div class="date-entry">
      <p class="date-entry__venue">The Lantern Room (Melbourne)</p>
      <p class="date-entry__when">Feb 23rd to the 26th</p>
    </div>
    <div class="date-entry">
      <p class="date-entry__venue">Le Corbeau, REVedge(Adelaide)</p>
      <p class="date-entry__when">March 3rd and 4th</p>
    </div>
  </section>

  <aside class="blurb">
    <div class="blurb__photo" role="img" aria-label="Photograph of the artist holding an open blank book"></div>
    <p>The last time someone showed you a little something they were working on, did you lose an hour of your life you will never get back? Don’t worry – we’ve all been there.</p>
    <p>Composer and co-writer of Rally! (A revue about lawn bowls) and WINNER of BEST CABARET, BEST WRITING and PEOPLE’S CHOICE awards at Quick + Tidy Revue 2011, presents her full show, with more original music and helpful anecdotes.</p>
  </aside>

  <p class="more-info">More info at www.mingleface.example/thevelvetparlour</p>
</main>
</body>
</html>
```